Heronbrook Custom Woodcraft Website design

Need a small website to showcase my products and take orders

would also like payment options

We do custom wood work along with cnc work in wood plastic and soft metals

we are based in edmonton alberta canada
Updates

Industry/Entity Type

Work

Number of Pages Required

3 page

Requirements
Nice to have
• Interview for for a woodworking magazine
• http://grainandplaneweekly.example/issue-1-02-august-2016/member-spotlight
• I would also like to see metal working/branding iron info
• Also adding the picture of me from the above interview is a nice touch

```html
<!DOCTYPE html>
<html lang="en">
<head>
<meta charset="utf-8">
<title>Heronbrook Custom Woodcraft</title>
<link rel="stylesheet" href="https://fonts.googleapis.com/css2?family=Cinzel:wght@400;700&family=Arimo:wght@400;700&display=swap">
<style>
:root{
  --cream:#f0d9c3;
  --cream-deep:#e8cdb4;
  --brown:#6f4f45;
  --brown-dark:#5c3f36;
  --brown-soft:#a47f6c;
  --ink:#5a3e35;
  --text:#7a5d52;
  --white:#ffffff;
  --rule:#d2b59d;
}
*{box-sizing:border-box;margin:0;padding:0}
html,body{width:1200px;height:2956px;overflow:hidden}
body{background:var(--cream);font-family:"Arimo",Arial,sans-serif;color:var(--text);position:relative}
.abs{position:absolute}
.serif{font-family:"Cinzel",Georgia,serif}

/* header */
.site-header{left:0;top:0;width:1200px;height:115px;background:var(--cream)}
.brand{left:78px;top:28px;display:flex;align-items:center;gap:14px}
.brand-dot{width:58px;height:58px;border-radius:50%;background:var(--brown)}
.brand-name{font-family:"Cinzel",Georgia,serif;font-size:26px;line-height:1.1;color:var(--brown);font-weight:400}
.brand-name small{display:block;font-size:14px;letter-spacing:2px}
.main-nav{left:530px;top:34px;display:flex;align-items:center}
.main-nav a{font-size:16px;color:var(--ink);text-decoration:none;margin-right:50px}
.main-nav a.active{background:var(--brown);color:var(--white);border-radius:26px;padding:15px 32px;margin-right:36px}

/* hero */
.hero{left:0;top:115px;width:1200px;height:563px;background:linear-gradient(135deg,#7a4a2a 0%,#c58a4a 30%,#e0b27a 55%,#c08650 80%,#8a5a34 100%)}
.hero-title{left:0;top:210px;width:1200px;display:flex;justify-content:center;align-items:center;gap:22px}
.hero-dot{width:84px;height:84px;border-radius:50%;background:var(--white)}
.hero-name{font-family:"Cinzel",Georgia,serif;color:var(--white);font-size:84px;line-height:0.95;font-weight:700;text-align:center}
.hero-name small{display:block;font-size:40px;letter-spacing:4px;font-weight:400}

/* pill button */
.pill{display:inline-flex;align-items:center;height:56px;border-radius:28px;background:var(--brown);color:var(--cream);font-family:"Cinzel",Georgia,serif;font-size:21px;padding-left:34px;gap:22px;white-space:nowrap}
.pill.light{background:var(--cream);color:var(--brown)}
.pill .knob{width:56px;height:56px;border-radius:50%;background:var(--cream);border:3px solid var(--brown);display:flex;align-items:center;justify-content:center}
.pill.light .knob{border-color:var(--cream);background:var(--white)}
.pill.small{height:46px;font-size:18px;padding-left:24px;gap:12px;border-radius:23px}
.pill.small .knob{width:46px;height:46px}

/* welcome */
.welcome{left:0;top:678px;width:1200px;height:380px;background:var(--brown);text-align:center}
.welcome .eyebrow{margin-top:62px;font-family:"Cinzel",Georgia,serif;font-size:16px;letter-spacing:2px;color:var(--brown-soft)}
.welcome h2{font-family:"Cinzel",Georgia,serif;font-weight:400;font-size:34px;color:var(--cream);margin-top:6px;letter-spacing:1px}
.welcome p{width:900px;margin:14px auto 0;font-size:14px;line-height:27px;color:var(--cream)}
.welcome .pill{margin-top:24px}

/* products */
.eyebrow-dark{font-family:"Cinzel",Georgia,serif;font-size:16px;letter-spacing:1px;color:var(--brown-soft)}
.section-title{font-family:"Cinzel",Georgia,serif;font-weight:700;font-size:32px;color:var(--ink);letter-spacing:1px}
.intro{left:78px;top:1120px;width:295px}
.intro p{font-size:14px;line-height:26px;color:var(--brown-soft);margin-top:12px}
.intro .pill{margin-top:26px;height:54px}
.product-grid{left:383px;top:1118px;width:741px;display:grid;grid-template-columns:repeat(3,240px);gap:12px 10px}
.product-card{height:322px;background:var(--brown);display:flex;flex-direction:column;align-items:center}
.product-photo{width:170px;height:170px;border-radius:50%;margin-top:24px;background:radial-gradient(circle,#c9a07a 0%,#a87a55 45%,var(--cream) 46%)}
.product-name{font-family:"Cinzel",Georgia,serif;font-size:19px;color:var(--cream);margin-top:22px}
.product-card .pill{margin-top:12px}

.rule{left:78px;width:1046px;height:1px;background:var(--rule)}

/* about */
.about-title{left:78px;top:1888px}
.about-photo{left:78px;top:1950px;width:312px;height:233px;background:linear-gradient(120deg,#3b2a22 0%,#6d5140 50%,#2a1f1a 100%)}
.about-copy{left:412px;top:1946px;width:712px}
.about-copy h3{font-family:"Cinzel",Georgia,serif;font-weight:400;font-size:22px;line-height:30px;color:var(--ink)}
.about-copy p{font-size:14px;line-height:26px;color:var(--text);margin-top:8px}
.about-copy .pill{margin-top:14px}

/* contact */
.contact{left:0;top:2330px;width:1200px;text-align:center}
.contact p{width:860px;margin:14px auto 0;font-size:14px;line-height:26px;color:var(--text)}
.contact-form{left:153px;top:2455px;width:893px}
.field-row{display:flex;gap:10px}
.field{flex:1;height:53px;border:1px solid var(--brown-soft);font-size:14px;color:var(--brown-soft);padding:16px 12px}
.field.active{background:var(--brown-soft);color:var(--white)}
.field.message{height:104px;margin-top:10px}
.submit{left:507px;top:2636px}

/* footer */
.site-footer{left:0;top:2757px;width:1200px;height:199px;background:var(--brown)}
.footer-nav{left:78px;top:2777px;display:flex;align-items:center}
.footer-nav a{font-size:14px;color:var(--cream);text-decoration:none;margin-right:44px}
.footer-nav a.active{border:1px solid var(--cream);border-radius:25px;padding:14px 20px;margin-right:36px}
.social{left:964px;top:2775px;display:flex;gap:10px}
.social span{width:48px;height:48px;border-radius:50%;background:var(--cream)}
.footer-info{left:78px;top:2868px;width:1050px;display:flex;align-items:center;font-size:14px;line-height:22px;color:var(--cream)}
.ico{width:48px;height:48px;border-radius:50%;border:1px solid var(--cream);display:flex;align-items:center;justify-content:center;flex:none;margin-right:16px}
.ico.fill{background:var(--cream);border:none}
</style>
</head>
<body>

<header class="site-header abs">
  <div class="brand abs">
    <span class="brand-dot"></span>
    <div class="brand-name">HERONBROOK<small>CUSTOM WOODCRAFT</small></div>
  </div>
  <nav class="main-nav abs">
    <a class="active" href="#">HOME</a>
    <a href="#">ABOUT</a>
    <a href="#">PRODUCT</a>
    <a href="#">NEWS</a>
    <a href="#">CONTACT</a>
  </nav>
</header>

<section class="hero abs" role="img" aria-label="Woodworking chisels and wood shavings on a pine workbench"></section>
<div class="hero-title abs">
  <span class="hero-dot"></span>
  <div class="hero-name">HERONBROOK<small>CUSTOM WOODCRAFT</small></div>
</div>
<div class="abs" style="left:430px;top:515px">
  <span class="pill" style="height:62px;border-radius:31px;background:var(--brown-dark)">CONTACT US KNOW
    <span class="knob" style="width:62px;height:62px"><svg width="18" height="18" viewBox="0 0 18 18"><path d="M6 3l6 6-6 6" stroke="#5c3f36" stroke-width="2.5" fill="none"/></svg></span>
  </span>
</div>

<section class="welcome abs">
  <div class="eyebrow">WELCOME TO</div>
  <h2>HERONBROOK CUSTOM WOODCRAFT</h2>
  <p>Lorem Ipsum is simply dummy text of the printing and typesetting industry. Lorem Ipsum has been the industry's standard dummy text ever since the 1500s, when an unknown printer took a galley of type and scrambled it to make a type specimen book. It has survived not only five It was popularised in the 1960s with the release of Letraset sheets containing Lorem Ipsum passages, and more recently with desktop publishing software like Folio Layout .</p>
  <span class="pill light">KNOW MORE
    <span class="knob"><svg width="16" height="16" viewBox="0 0 18 18"><path d="M6 3l6 6-6 6" stroke="#6f4f45" stroke-width="2.5" fill="none"/></svg></span>
  </span>
</section>

<section class="intro abs">
  <div class="eyebrow-dark">WHAT WE PROVIDE</div>
  <h2 class="section-title" style="margin-top:14px">OUR PRODUCT</h2>
  <p>Lorem Ipsum is simply dummy text of the printing and typesetting industry. Lorem Ipsum has been the industry's standard dummy text ever since..</p>
  <p>Lorem Ipsum is simply dummy text of the printing and typesetting industry. Lorem Ipsum has been the industry's standard dummy text ever since</p>
  <p style="margin-top:20px">Lorem Ipsum is simply dummy text of the printing and typesetting industry. Lorem Ipsum has been the industry's standard dummy text ever since..</p>
  <p>Lorem Ipsum is simply dummy text of the printing and typesetting industry. Lorem Ipsum has been the industry's standard dummy text ever since</p>
  <span class="pill">KNOW MORE
    <span class="knob"><svg width="16" height="16" viewBox="0 0 18 18"><path d="M6 3l6 6-6 6" stroke="#6f4f45" stroke-width="2.5" fill="none"/></svg></span>
  </span>
</section>

<section class="product-grid abs">
  <article class="product-card"><div class="product-photo" role="img" aria-label="Folding wooden stool"></div><div class="product-name">PRODUCT NAME</div><span class="pill small light">ODER KNOW<span class="knob"><svg width="14" height="14" viewBox="0 0 18 18"><path d="M6 3l6 6-6 6" stroke="#6f4f45" stroke-width="2.5" fill="none"/></svg></span></span></article>
  <article class="product-card"><div class="product-photo" role="img" aria-label="Wooden step stool"></div><div class="product-name">PRODUCT NAME</div><span class="pill small light">ODER KNOW<span class="knob"><svg width="14" height="14" viewBox="0 0 18 18"><path d="M6 3l6 6-6 6" stroke="#6f4f45" stroke-width="2.5" fill="none"/></svg></span></span></article>
  <article class="product-card"><div class="product-photo" role="img" aria-label="Oval carved wooden bowl"></div><div class="product-name">PRODUCT NAME</div><span class="pill small light">ODER KNOW<span class="knob"><svg width="14" height="14" viewBox="0 0 18 18"><path d="M6 3l6 6-6 6" stroke="#6f4f45" stroke-width="2.5" fill="none"/></svg></span></span></article>
  <article class="product-card"><div class="product-photo" role="img" aria-label="Pair of wooden serving trays"></div><div class="product-name">PRODUCT NAME</div><span class="pill small light">ODER KNOW<span class="knob"><svg width="14" height="14" viewBox="0 0 18 18"><path d="M6 3l6 6-6 6" stroke="#6f4f45" stroke-width="2.5" fill="none"/></svg></span></span></article>
  <article class="product-card"><div class="product-photo" role="img" aria-label="Engraved round wooden plaque"></div><div class="product-name">PRODUCT NAME</div><span class="pill small light">ODER KNOW<span class="knob"><svg width="14" height="14" viewBox="0 0 18 18"><path d="M6 3l6 6-6 6" stroke="#6f4f45" stroke-width="2.5" fill="none"/></svg></span></span></article>
  <article class="product-card"><div class="product-photo" role="img" aria-label="Wooden step stool"></div><div class="product-name">PRODUCT NAME</div><span class="pill small light">ODER KNOW<span class="knob"><svg width="14" height="14" viewBox="0 0 18 18"><path d="M6 3l6 6-6 6" stroke="#6f4f45" stroke-width="2.5" fill="none"/></svg></span></span></article>
</section>

<div class="rule abs" style="top:1840px"></div>

<h2 class="section-title about-title abs">ABOUT US</h2>
<div class="about-photo abs" role="img" aria-label="The craftsman standing in his workshop beside hanging tack"></div>
<section class="about-copy abs">
  <h3>WHAT IS YOUR “INSPIRATION STORY” — WHERE DID YOUR INTEREST IN WOODWORKING ALL BEGIN?</h3>
  <p>&nbsp;grew up in a small logging community in &nbsp;British Columbia Canada. Wood and woodworking were always around. With no Big Box stores around, I developed an “I can do that” attitude: need something, build it; doesn’t work, rebuild it.</p>
  <p style="margin-top:26px">Some of my fondest memories are of watching my father in the shop.</p>
  <span class="pill">KNOW MORE
    <span class="knob"><svg width="16" height="16" viewBox="0 0 18 18"><path d="M6 3l6 6-6 6" stroke="#6f4f45" stroke-width="2.5" fill="none"/></svg></span>
  </span>
</section>

<div class="rule abs" style="top:2275px"></div>

<section class="contact abs">
  <h2 class="section-title">CONTACT US</h2>
  <p>Lorem Ipsum is simply dummy text of the printing and typesetting industry. Lorem Ipsum has been the industry's standard dummy text ever since the 1500s, when an unknown printer took.</p>
</section>
<form class="contact-form abs">
  <div class="field-row">
    <div class="field active">Name*</div>
    <div class="field">Email*</div>
    <div class="field">Phone*</div>
  </div>
  <div class="field message">Message*</div>
</form>
<div class="submit abs">
  <span class="pill" style="padding-left:30px">SUBMIT
    <span class="knob"><svg width="16" height="16" viewBox="0 0 18 18"><path d="M6 3l6 6-6 6" stroke="#6f4f45" stroke-width="2.5" fill="none"/></svg></span>
  </span>
</div>

<footer class="site-footer abs"></footer>
<nav class="footer-nav abs">
  <a class="active" href="#">Home</a>
  <a href="#">About</a>
  <a href="#">Product</a>
  <a href="#">News</a>
  <a href="#">Contact</a>
</nav>
<div class="social abs" aria-label="Social links"><span></span><span></span><span></span></div>
<div class="footer-info abs">
  <span class="ico fill"><svg width="20" height="24" viewBox="0 0 20 24"><path d="M10 1a8 8 0 0 0-8 8c0 6 8 14 8 14s8-8 8-14a8 8 0 0 0-8-8z" fill="#6f4f45"/><circle cx="10" cy="9" r="3" fill="#f0d9c3"/></svg></span>
  <span style="width:210px">Lorem Ipsum is simply dummy text of the printing.</span>
  <span class="ico" style="margin-left:8px"><svg width="22" height="22" viewBox="0 0 24 24"><path d="M5 3h4l2 5-3 2a12 12 0 0 0 6 6l2-3 5 2v4a2 2 0 0 1-2 2A18 18 0 0 1 3 5a2 2 0 0 1 2-2z" fill="none" stroke="#f0d9c3" stroke-width="1.6"/></svg></span>
  <span style="width:190px">123 - 456 - 7890</span>
  <span class="ico"><svg width="22" height="16" viewBox="0 0 22 16"><rect x="1" y="1" width="20" height="14" fill="none" stroke="#f0d9c3" stroke-width="1.6"/><path d="M1 1l10 8 10-8" fill="none" stroke="#f0d9c3" stroke-width="1.6"/></svg></span>
  <span style="width:200px">info@heronbrook.example</span>
  <span style="width:270px">© HERONBROOK CUSTOM WOODCRAFT - 2016 All rights reserved</span>
</div>

</body>
</html>
```